Dental Office Business Card

We need a business card for our pediatric dentistry office.
On one side the design needs to contain the following:
our logo (attached)
Vento Pediatric Grins
Soraya Kadbelani, DDS
Board Certified Pediatric Dentist
Tel: (555) 318-2747)
Fax: (555) 264-8031
Email: info@ventopediatricgrins.example
Web: www.ventopediatricgrins.example
Address: 41 Brindle Ave, Suite 208, Wellesley, MA 02099

On the other side of the card, the design needs to have an appointment reminder (date and time as well as day of the week) similar to the design attached (no need for appointment reason “For”)

```html
<!DOCTYPE html>
<html lang="en">
<head>
<meta charset="utf-8">
<title>Vento Pediatric Grins – Business Card</title>
<link rel="stylesheet" href="https://fonts.googleapis.com/css2?family=Poppins:ital,wght@0,300;0,400;0,600;0,700;1,300;1,400&display=swap">
<style>
  :root {
    --mint: #a6d5a8;
    --ink: #0a0a0a;
    --text: #1f1f1f;
    --paper: #ffffff;
    --back-paper: #f2f8f3;
    --stage: #ffffff;
  }
  * { box-sizing: border-box; margin: 0; padding: 0; }
  html, body { width: 960px; height: 1200px; overflow: hidden; }
  body { background: var(--stage); font-family: "Poppins", sans-serif; color: var(--text); position: relative; }

  .card { position: absolute; left: 60px; width: 840px; height: 480px; overflow: hidden; }
  .card--front { top: 94px; background: var(--paper); }
  .card--back { top: 626px; background: var(--back-paper); }

  .band { position: absolute; left: 0; width: 100%; background: var(--ink); }
  .card--front .band { top: 61px; height: 43px; }
  .card--back .band { top: 62px; height: 44px; }

  .blob { position: absolute; left: 0; top: 0; width: 840px; height: 480px; }

  .brand { position: absolute; left: 52px; top: 222px; display: flex; align-items: center; gap: 10px; }
  .brand-dot { width: 16px; height: 16px; border-radius: 50%; background: var(--ink); flex: none; }
  .brand-name { font-weight: 700; font-size: 22px; line-height: 1.15; color: var(--ink); }

  .dentist-name { position: absolute; left: 410px; top: 72px; font-weight: 700; font-size: 22px; color: var(--mint); white-space: nowrap; }
  .credential { position: absolute; left: 410px; top: 113px; font-size: 11.5px; font-weight: 400; white-space: nowrap; }
  .credential-rule { position: absolute; left: 608px; top: 121px; width: 206px; height: 1.5px; background: var(--mint); }

  .contact { position: absolute; left: 410px; display: flex; align-items: center; font-weight: 300; font-size: 19px; white-space: nowrap; }
  .contact svg { width: 27px; height: 27px; flex: none; margin-right: 19px; }
  .contact--address { top: 186px; align-items: flex-start; line-height: 24px; }
  .contact--address svg { margin-top: -2px; }
  .contact--phone { top: 290px; }
  .contact--email { top: 326px; }
  .contact--fax { top: 362px; }
  .contact--web { top: 397px; }

  .reminder-title { position: absolute; left: 0; top: 58px; width: 100%; text-align: center; font-weight: 300; font-size: 46px; letter-spacing: 12px; color: var(--mint); line-height: 52px; padding-left: 12px; }
  .reminder-sub { position: absolute; left: 0; top: 116px; width: 100%; text-align: center; font-style: italic; font-weight: 400; font-size: 30px; letter-spacing: 7px; color: var(--ink); padding-left: 7px; }

  .field-label { position: absolute; left: 90px; font-size: 29px; font-weight: 300; color: var(--ink); }
  .field-label--date { top: 180px; }
  .field-label--time { top: 365px; }
  .field-line { position: absolute; left: 201px; height: 1.5px; background: var(--ink); }
  .field-line--date { top: 210px; width: 493px; }
  .field-line--time { top: 394px; width: 189px; }
  .meridiem { position: absolute; left: 414px; top: 370px; font-style: italic; font-weight: 300; font-size: 24px; word-spacing: 8px; }

  .day { position: absolute; top: 278px; display: flex; align-items: flex-end; font-style: italic; font-weight: 300; font-size: 25px; line-height: 1; color: var(--ink); }
  .day-box { width: 28px; height: 28px; border: 1.5px solid var(--ink); margin-right: 4px; }
</style>
</head>
<body>

<section class="card card--front">
  <div class="band"></div>
  <svg class="blob" viewBox="0 0 840 480" aria-hidden="true">
    <path fill="#a6d5a8" d="M140,0 L312,0 C335,20 340,60 334,106 C328,170 290,220 296,266 C300,310 345,335 352,380 C358,420 366,450 364,480 L276,480 C240,430 190,350 110,358 C50,362 20,420 0,450 L0,129 C40,125 70,100 100,50 Z"/>
  </svg>

  <div class="brand">
    <span class="brand-dot"></span>
    <span class="brand-name">Vento<br>Pediatric Grins</span>
  </div>

  <h1 class="dentist-name">Soraya Kadbelani, DDS</h1>
  <p class="credential">Board Certified Pediatric Dentist</p>
  <div class="credential-rule"></div>

  <div class="contact contact--address">
    <svg viewBox="0 0 28 28" aria-hidden="true"><circle cx="14" cy="14" r="14" fill="#a6d5a8"/><path fill="#fff" d="M14 6.5a5 5 0 0 0-5 5c0 3.6 5 9.5 5 9.5s5-5.9 5-9.5a5 5 0 0 0-5-5zm0 7a2 2 0 1 1 0-4 2 2 0 0 1 0 4z"/></svg>
    <span>41 Brindle Ave,<br>Suite 208, Wellesley,<br>MA 02099</span>
  </div>
  <div class="contact contact--phone">
    <svg viewBox="0 0 28 28" aria-hidden="true"><circle cx="14" cy="14" r="14" fill="#a6d5a8"/><path fill="#fff" d="M10.2 7.5l2 3.2-1.3 1.5c.9 1.9 2.3 3.3 4.2 4.2l1.5-1.3 3.2 2-.9 2.6c-5.5-.3-9.6-4.4-9.9-9.9z"/></svg>
    <span>(555) 318-2747)</span>
  </div>
  <div class="contact contact--email">
    <svg viewBox="0 0 28 28" aria-hidden="true"><circle cx="14" cy="14" r="14" fill="#a6d5a8"/><rect x="7.5" y="9.5" width="13" height="9" fill="none" stroke="#fff" stroke-width="1.4"/><path d="M7.5 9.5l6.5 5 6.5-5" fill="none" stroke="#fff" stroke-width="1.4"/></svg>
    <span>info@ventopediatricgrins.example</span>
  </div>
  <div class="contact contact--fax">
    <svg viewBox="0 0 28 28" aria-hidden="true"><circle cx="14" cy="14" r="14" fill="#a6d5a8"/><rect x="10" y="7" width="8" height="5" fill="none" stroke="#fff" stroke-width="1.3"/><rect x="7.5" y="12" width="13" height="6" fill="#fff"/><rect x="10" y="17" width="8" height="4.5" fill="#a6d5a8" stroke="#fff" stroke-width="1.3"/></svg>
    <span>(555) 264-8031</span>
  </div>
  <div class="contact contact--web">
    <svg viewBox="0 0 28 28" aria-hidden="true"><circle cx="14" cy="14" r="14" fill="#a6d5a8"/><g fill="none" stroke="#fff" stroke-width="1.2"><circle cx="14" cy="14" r="6.5"/><ellipse cx="14" cy="14" rx="2.8" ry="6.5"/><path d="M7.5 14h13M8.5 10.5h11M8.5 17.5h11"/></g></svg>
    <span>www.ventopediatricgrins.example</span>
  </div>
</section>

<section class="card card--back">
  <div class="band"></div>
  <h2 class="reminder-title">APPOINTMENT</h2>
  <p class="reminder-sub">REMINDER</p>

  <span class="field-label field-label--date">date :</span>
  <div class="field-line field-line--date"></div>

  <div class="day" style="left:90px"><span class="day-box"></span>mon</div>
  <div class="day" style="left:201px"><span class="day-box"></span>tue</div>
  <div class="day" style="left:293px"><span class="day-box"></span>wed</div>
  <div class="day" style="left:398px"><span class="day-box"></span>thurs</div>
  <div class="day" style="left:516px"><span class="day-box"></span>fri</div>
  <div class="day" style="left:586px"><span class="day-box"></span>sat</div>
  <div class="day" style="left:674px"><span class="day-box"></span>sun</div>

  <span class="field-label field-label--time">time :</span>
  <div class="field-line field-line--time"></div>
  <span class="meridiem">a.m. p.m.</span>
</section>

</body>
</html>
```